Official personalized stationery with official coat of arms

I am looking for custom stationery design such as US letter size (8.5 X 11 or 21.6cm X 27.9cm), email signature (email) and envelope for US letter size (standard envelope no. 10 or 10.5cm X 24.5cm). Inspired by my personal coat of arms and my postal address:

4186 rue des Tilleuls
Levis, Quebec, H2K 4P7
Canada

Ideally a discreet design based on the coat of arms of Lucien Morvan but inspired by my mother's original coat of arms.

Something golden and translucent, simple but tasteful, without overemphasizing the green color. The coat of arms should have green, but not the entire structure of the stationery.

I am also looking for a small official thank you card in half letter size.

The design must be with the Lucien Morvan coat of arms and not the full coat of arms

Target Market(s)

For official communication

Industry/Entity Type

Communication officiel et parlementaire

Font styles to use
Other font styles liked:
• J’aime bien l’écriture comme le logo de la maison Delorme la police pour écrire le nom Delorme

Requirements
Must have
• Simplicity and use the Lucien Morvan coat of arms and not the full coat of arms
Nice to have
• Official and royal appearance as it is an official heraldic title of the British crown
Should not have
• Email and website

```html
<!DOCTYPE html>
<html lang="fr">
<head>
<meta charset="utf-8">
<title>Lucien Morvan — Stationery Set</title>
<link href="https://fonts.googleapis.com/css2?family=Lora:wght@400;600;700&display=swap" rel="stylesheet">
<style>
  :root {
    --board: #e2e2e3;
    --paper: #ffffff;
    --green: #1f5a1c;
    --gold: #c49a3c;
    --gold-rule: #b88d2e;
    --ink: #1d1d1d;
    --muted: #4a4a4a;
    --edge: #cfcfcf;
    --shadow: rgba(0,0,0,0.18);
  }
  * { margin: 0; padding: 0; box-sizing: border-box; }
  html, body { width: 1200px; height: 900px; overflow: hidden; }
  body {
    background: var(--board);
    font-family: "Lora", Georgia, serif;
    color: var(--ink);
    position: relative;
  }
  .sheet {
    position: absolute;
    background: var(--paper);
    box-shadow: 0 1px 3px var(--shadow);
  }
  .mark {
    position: absolute;
    display: flex;
    flex-direction: column;
    align-items: center;
    justify-content: center;
    gap: 6px;
    color: var(--green);
    font-family: "Lora", Georgia, serif;
    font-weight: 600;
    text-align: center;
    line-height: 1.15;
  }
  .mark .dot {
    border-radius: 50%;
    background: var(--gold);
  }
  .rule {
    position: absolute;
    background: var(--gold-rule);
  }
  .address {
    position: absolute;
    text-align: center;
    white-space: nowrap;
  }

  /* Letterhead */
  .letterhead { left: 57px; top: 102px; width: 535px; height: 691px; }
  .letterhead .mark { left: 210px; top: 25px; width: 115px; height: 155px; font-size: 17px; }
  .letterhead .mark .dot { width: 14px; height: 14px; }
  .letterhead .rule { left: 74px; top: 658px; width: 386px; height: 2.5px; }
  .letterhead .address { left: 0; width: 100%; top: 668px; font-size: 9.5px; }

  /* Envelope front */
  .envelope-front { left: 671px; top: 103px; width: 471px; height: 235px; overflow: hidden; }
  .envelope-front .mark { left: 26px; top: 22px; width: 80px; height: 105px; font-size: 12px; }
  .envelope-front .mark .dot { width: 10px; height: 10px; }
  .envelope-front .mark-faint {
    left: 316px; top: 8px; width: 150px; height: 196px;
    font-size: 22px; opacity: 0.1;
    color: var(--gold);
  }
  .envelope-front .mark-faint .dot { width: 20px; height: 20px; }
  .envelope-front .rule { left: 30px; top: 204px; width: 410px; height: 1.5px; }
  .envelope-front .address { left: 30px; top: 213px; font-size: 8px; text-align: left; }

  /* Envelope back */
  .envelope-back { left: 671px; top: 370px; width: 471px; height: 235px; }
  .envelope-back .flap { position: absolute; left: 0; top: 0; width: 471px; height: 70px; }
  .envelope-back .mark { left: 204px; top: 10px; width: 60px; height: 44px; font-size: 7.5px; gap: 3px; }
  .envelope-back .mark .dot { width: 6px; height: 6px; }

  /* Business card */
  .business-card { left: 671px; top: 648px; width: 264px; height: 132px; }
  .business-card .mark { left: 34px; top: 24px; width: 58px; height: 74px; font-size: 9px; gap: 4px; }
  .business-card .mark .dot { width: 7px; height: 7px; }
  .card-name { position: absolute; left: 139px; top: 32px; font-size: 8.5px; font-weight: 700; }
  .card-role { position: absolute; left: 139px; top: 43px; font-size: 6px; color: var(--muted); }
  .card-role-rule { position: absolute; left: 139px; top: 52px; width: 23px; height: 1px; background: var(--gold-rule); }
  .contact-list { position: absolute; left: 139px; top: 60px; list-style: none; font-size: 6px; line-height: 8.7px; }
  .contact-list li { display: flex; align-items: center; gap: 4px; }
  .contact-list svg { width: 5px; height: 5px; fill: var(--gold); flex: none; }
  .business-card .rule { left: 20px; top: 114px; width: 224px; height: 1px; }
  .business-card .address { left: 0; width: 100%; top: 119px; font-size: 5.6px; }
</style>
</head>
<body>

  <section class="sheet letterhead" aria-label="Letterhead">
    <div class="mark" role="img" aria-label="Lucien Morvan coat of arms">
      <span class="dot"></span>
      <span>Lucien<br>Morvan</span>
    </div>
    <div class="rule"></div>
    <p class="address">4186 rue des Tilleuls Levis, Quebec, H2K 4P7, Canada</p>
  </section>

  <section class="sheet envelope-front" aria-label="Envelope front">
    <div class="mark" role="img" aria-label="Lucien Morvan coat of arms">
      <span class="dot"></span>
      <span>Lucien<br>Morvan</span>
    </div>
    <div class="mark mark-faint" aria-hidden="true">
      <span class="dot"></span>
      <span>Lucien<br>Morvan</span>
    </div>
    <div class="rule"></div>
    <p class="address">4186 rue des Tilleuls Levis, Quebec, H2K 4P7, Canada</p>
  </section>

  <section class="sheet envelope-back" aria-label="Envelope back">
    <svg class="flap" viewBox="0 0 471 70" aria-hidden="true">
      <path d="M3 2 Q6 55 12 62 Q15 66 24 66 L455 66 Q464 66 466 60 Q469 50 470 2"
            fill="none" stroke="var(--edge)" stroke-width="1"/>
    </svg>
    <div class="mark" role="img" aria-label="Lucien Morvan coat of arms">
      <span class="dot"></span>
      <span>Lucien<br>Morvan</span>
    </div>
  </section>

  <section class="sheet business-card" aria-label="Business card">
    <div class="mark" role="img" aria-label="Lucien Morvan coat of arms">
      <span class="dot"></span>
      <span>Lucien<br>Morvan</span>
    </div>
    <p class="card-name">Étienne Vachon</p>
    <p class="card-role">Owner</p>
    <div class="card-role-rule"></div>
    <ul class="contact-list">
      <li><svg viewBox="0 0 10 10"><rect x="2.5" y="0.5" width="5" height="9" rx="1" fill="none" stroke="var(--gold)" stroke-width="1.2"/></svg>418-555-0162</li>
      <li><svg viewBox="0 0 10 10"><path d="M1 4 Q5 0 9 4 L8 5.5 L6.5 4.5 L3.5 4.5 L2 5.5 Z M2.5 6 L7.5 6 L8.5 9 L1.5 9 Z"/></svg>418-555-0179</li>
    </ul>
    <div class="rule"></div>
    <p class="address">4186 rue des Tilleuls Levis, Quebec, H2K 4P7, Canada</p>
  </section>

</body>
</html>
```